Designs of screens for job search mobile app

Design the following screens:

1. Login
2. Job search results in tabs
3. Job details in cards format
4. Profile
5. Settings

Logo and references are provided. The app need to be playful, easy to use, different from traditional job search app like Hirevo, Workbrix and others and targeted to Millennial users (age 18-30).

The main app reference is Pogura, in terms of the colorful and fun color and font scheme.

Target Market(s)

Millennial users (age 18-30).

Requirements
Must have
• A fun, playful feel

```html
<!DOCTYPE html>
<html lang="en">
<head>
<meta charset="utf-8">
<title>JobRover – mobile app screens</title>
<link href="https://fonts.googleapis.com/css2?family=Source+Sans+3:wght@400;600;700&display=swap" rel="stylesheet">
<style>
:root{
  --orange:#F7941D;
  --teal:#12B5B5;
  --ink:#4D4D4D;
  --slate:#58595B;
  --mist:#E6E6E6;
  --paper:#FFFFFF;
  --alert:#E0262B;
  --sun:#FBB321;
}
*{box-sizing:border-box;margin:0;padding:0}
html,body{width:1200px;height:1200px;overflow:hidden;background:var(--paper);font-family:"Source Sans 3",Arial,sans-serif}
.board{position:absolute;left:0;top:0;width:1500px;height:1500px;transform:scale(.8);transform-origin:0 0}
.screen{position:absolute;width:249px;background:var(--paper);border:1px solid #777;overflow:hidden}
.abs{position:absolute}
.brand{position:absolute;left:0;right:0;display:flex;align-items:center;justify-content:center;gap:8px;font-weight:600;color:var(--ink);font-size:30px;letter-spacing:-.5px}
.brand i{display:block;width:26px;height:26px;border-radius:50%;background:var(--teal)}
.brand.on-color i{background:var(--paper)}
.titlebar{position:absolute;left:0;right:0;top:72px;height:36px;background:var(--orange);color:#fff;font-weight:700;font-size:20px;display:flex;align-items:center;justify-content:center}
.back{position:absolute;left:10px;top:6px;width:24px;height:24px}
.nav{position:absolute;left:0;right:0;display:flex;justify-content:space-around;padding:0 6px}
.nav svg{width:37px;height:37px}
.field{position:absolute;left:7px;width:228px;height:37px;border:1px solid var(--orange);font-size:11px;color:var(--ink);display:flex;align-items:center;padding-left:9px}
.field b{color:var(--orange);font-weight:600;margin-right:3px}
.btn{position:absolute;background:var(--orange);color:#fff;font-weight:700;display:flex;align-items:center;justify-content:center}
.result{position:absolute;left:0;width:248px;height:86px}
.result.teal{background:var(--teal)}
.result.pale{background:#F2F2F2}
.thumb{position:absolute;left:20px;top:12px;width:56px;height:56px;border-radius:50%;background:var(--orange)}
.facts{position:absolute;left:97px;top:0;width:151px;font-size:10px}
.facts div{height:25px;border-bottom:1px solid rgba(255,255,255,.7);padding:3px 4px 0}
.facts .lead{height:17px;padding-top:2px;color:#222;font-weight:600}
.facts .val{color:var(--orange)}
.result.pale .facts .val{color:var(--teal)}
.result.pale .facts div{border-color:#ddd}
.facts .when{height:16px;border:0;text-align:right;color:var(--orange);padding-top:1px}
.row-list div{position:absolute;left:4px;right:4px;height:37px;border-bottom:2px solid var(--orange);color:var(--teal);font-size:10px;font-weight:600;display:flex;align-items:center;justify-content:space-between;padding:0 6px 0 18px}
.row-list svg{width:24px;height:24px}
.form-field{position:absolute;left:11px;width:228px;height:36px;border:1px solid #bbb;border-bottom:2px solid var(--orange);color:var(--orange);font-size:11px;font-weight:600;display:flex;align-items:center;justify-content:space-between;padding:0 8px}
.chip{position:absolute;width:79px;height:36px;background:var(--orange);color:#fff;font-size:10px;font-weight:600;display:flex;align-items:center;justify-content:space-between;padding:0 6px 0 9px}
.setting{position:absolute;left:12px;font-size:13px;color:#222}
.setting.strong{font-weight:600}
.rule{position:absolute;left:3px;right:3px;height:2px;background:var(--orange)}
</style>
</head>
<body>
<svg width="0" height="0" style="position:absolute">
  <defs>
    <symbol id="i-home" viewBox="0 0 36 36"><circle cx="18" cy="18" r="17" fill="#12B5B5"/><path d="M9 19 18 10 27 19M12.5 16.5V27h11V16.5" fill="none" stroke="#fff" stroke-width="2.6" stroke-linejoin="round"/></symbol>
    <symbol id="i-search" viewBox="0 0 36 36"><circle cx="18" cy="18" r="17" fill="#12B5B5"/><circle cx="16" cy="16" r="6.5" fill="none" stroke="#fff" stroke-width="2.8"/><path d="M21 21l6 6" stroke="#fff" stroke-width="3.2" stroke-linecap="round"/></symbol>
    <symbol id="i-target" viewBox="0 0 36 36"><circle cx="18" cy="18" r="17" fill="#12B5B5"/><g fill="none" stroke="#fff" stroke-width="2"><circle cx="18" cy="18" r="9"/><circle cx="18" cy="18" r="5"/></g><path d="M18 18 27 9" stroke="#fff" stroke-width="2.2"/></symbol>
    <symbol id="i-doc" viewBox="0 0 36 36"><circle cx="18" cy="18" r="17" fill="#12B5B5"/><rect x="12" y="8.5" width="12" height="19" rx="1.5" fill="none" stroke="#fff" stroke-width="2.2"/><path d="M15 13.5h6M15 17.5h6M15 21.5h6" stroke="#fff" stroke-width="1.8"/></symbol>
    <symbol id="i-gear" viewBox="0 0 36 36"><circle cx="18" cy="18" r="17" fill="#12B5B5"/><circle cx="18" cy="18" r="9.5" fill="none" stroke="#fff" stroke-width="3.5" stroke-dasharray="3.3 2.6"/><circle cx="18" cy="18" r="7" fill="#fff"/><circle cx="18" cy="18" r="3" fill="#12B5B5"/></symbol>
    <symbol id="i-back" viewBox="0 0 24 24"><circle cx="12" cy="12" r="11.5" fill="#58595B"/><path d="M13.5 7.5 9 12l4.5 4.5" fill="none" stroke="#fff" stroke-width="1.6"/></symbol>
    <symbol id="i-plus" viewBox="0 0 24 24"><circle cx="12" cy="12" r="11.5" fill="#F7941D"/><path d="M12 6v12M6 12h12" stroke="#fff" stroke-width="2"/></symbol>
    <symbol id="i-tplus" viewBox="0 0 24 24"><circle cx="12" cy="12" r="11.5" fill="#12B5B5"/><path d="M12 6v12M6 12h12" stroke="#fff" stroke-width="2"/></symbol>
    <symbol id="i-tedit" viewBox="0 0 24 24"><circle cx="12" cy="12" r="11.5" fill="#12B5B5"/><path d="M8 16l1-3 6-6 2 2-6 6z" fill="#fff"/></symbol>
    <symbol id="i-ttrash" viewBox="0 0 24 24"><circle cx="12" cy="12" r="11.5" fill="#12B5B5"/><path d="M8 8h8M10 8V6.5h4V8M9 9.5h6l-.6 8h-4.8z" fill="none" stroke="#fff" stroke-width="1.4"/></symbol>
    <symbol id="i-x" viewBox="0 0 12 12"><path d="M1.5 1.5l9 9M10.5 1.5l-9 9" stroke="#fff" stroke-width="1.8"/></symbol>
    <symbol id="i-save" viewBox="0 0 52 52"><circle cx="26" cy="26" r="25" fill="#FBB321" stroke="#F7941D" stroke-width="2"/><rect x="15" y="15" width="22" height="22" rx="3" fill="none" stroke="#fff" stroke-width="3"/><path d="M19 15v6h12v-6M19 28h14M19 32h14" stroke="#fff" stroke-width="2.4" fill="none"/></symbol>
    <symbol id="i-next" viewBox="0 0 24 24"><circle cx="12" cy="12" r="11.5" fill="#F7941D"/><path d="M10 7.5 14.5 12 10 16.5" fill="none" stroke="#fff" stroke-width="2"/></symbol>
    <symbol id="i-skip" viewBox="0 0 36 36"><circle cx="18" cy="18" r="17" fill="#FBB321" stroke="#F7941D" stroke-width="1.5"/><path d="M11 12l6 6-6 6M18 12l6 6-6 6" fill="none" stroke="#fff" stroke-width="2.6"/></symbol>
    <symbol id="i-edit" viewBox="0 0 36 36"><circle cx="18" cy="18" r="17" fill="#E0262B"/><rect x="10" y="12" width="13" height="14" fill="none" stroke="#fff" stroke-width="2"/><path d="M16 20l1-3 8-8 2 2-8 8z" fill="#fff"/></symbol>
  </defs>
</svg>

<main class="board">

  <!-- Loading -->
  <section class="screen" style="left:43px;top:120px;height:410px">
    <div class="abs" style="left:6px;top:6px;width:236px;height:397px;background:var(--orange)"></div>
    <div class="brand on-color" style="top:82px;font-size:34px"><i></i>JobRover</div>
    <div class="abs" style="left:14px;top:227px;width:218px;height:47px;border:3px solid var(--teal);background:var(--orange)">
      <div class="abs" style="left:4px;top:4px;width:152px;height:33px;background:#fff"></div>
    </div>
    <div class="abs" style="left:0;right:0;top:292px;text-align:center;color:#fff;font-size:23px">LOADING...</div>
  </section>

  <!-- Sign in -->
  <section class="screen" style="left:304px;top:120px;height:410px">
    <div class="brand" style="top:12px;font-size:34px"><i></i>JobRover</div>
    <div class="abs" style="left:0;right:0;top:135px;height:117px;background:var(--teal)">
      <div class="brand on-color" style="top:15px;font-size:34px"><i></i>JobRover</div>
      <div class="abs" style="right:10px;top:63px;color:#fff;font-weight:600;font-size:13px;text-align:right;line-height:31px">Wondering where<br>to find talent!!!</div>
    </div>
    <div class="abs" style="left:80px;top:259px;display:flex;gap:12px">
      <span style="width:16px;height:16px;border-radius:50%;border:2px solid var(--orange)"></span>
      <span style="width:16px;height:16px;border-radius:50%;background:var(--teal)"></span>
      <span style="width:16px;height:16px;border-radius:50%;border:2px solid var(--orange)"></span>
      <span style="width:16px;height:16px;border-radius:50%;border:2px solid var(--orange)"></span>
    </div>
    <div class="titlebar" style="top:299px">Sign In</div>
    <div class="btn" style="left:21px;top:347px;width:42px;height:45px;background:#3B5998;font-size:7px;font-weight:600">Chatterly</div>
    <div class="btn" style="left:78px;top:347px;width:42px;height:45px;background:#1DA1F2;font-size:7px;font-weight:600">Birdline</div>
    <div class="btn" style="left:135px;top:347px;width:42px;height:45px;background:#DD4B39;font-size:7px;font-weight:600">Glocal</div>
    <div class="btn" style="left:192px;top:347px;width:42px;height:45px;background:#0077B5;font-size:7px;font-weight:600">Workbrix</div>
  </section>

  <!-- Search -->
  <section class="screen" style="left:580px;top:120px;height:410px">
    <div class="brand" style="top:24px"><i></i>JobRover</div>
    <div class="titlebar">Search<svg class="back"><use href="#i-back"/></svg></div>
    <div class="field" style="top:150px"><b>Jobs:</b>Job title, keywords, or company</div>
    <div class="field" style="top:216px"><b>Country:</b>Singapore</div>
    <div class="field" style="top:282px"><b>Location:</b>Singapore</div>
    <div class="btn" style="left:8px;top:332px;width:228px;height:23px;font-size:9px;font-weight:600">SEARCH JOBS</div>
    <nav class="nav" style="top:366px"><svg><use href="#i-home"/></svg><svg><use href="#i-search"/></svg><svg><use href="#i-target"/></svg><svg><use href="#i-doc"/></svg><svg><use href="#i-gear"/></svg></nav>
  </section>

  <!-- Search results -->
  <section class="screen" style="left:856px;top:120px;height:450px">
    <div class="brand" style="top:24px"><i></i>JobRover</div>
    <div class="titlebar">Search<svg class="back"><use href="#i-back"/></svg></div>
    <div class="abs" style="left:0;right:0;top:111px;height:24px;background:var(--slate);color:var(--orange);font-weight:600;font-size:13px;text-align:center;line-height:26px">Search Results</div>
    <div class="result teal" style="top:135px"><div class="thumb"></div><div class="facts"><div class="lead">Software Engineers</div><div class="val">Singapore</div><div class="val">$80 - $90 K per annum</div><div class="when">10 hrs ago</div></div></div>
    <div class="result pale" style="top:221px"><div class="thumb" style="top:15px"></div><div class="facts"><div class="lead" style="height:23px;padding-top:4px">System Architect</div><div class="val">Singapore</div><div class="val">$80 - $90 K per annum</div><div class="when" style="height:14px">1 day ago</div></div></div>
    <div class="result teal" style="top:307px"><div class="thumb" style="top:18px"></div><div class="facts"><div class="lead">Kava Developer</div><div class="val">Singapore</div><div class="val">$120 - $150 K per annum</div><div class="when">1 day ago</div></div></div>
    <nav class="nav" style="top:403px"><svg><use href="#i-home"/></svg><svg><use href="#i-search"/></svg><svg><use href="#i-target"/></svg><svg><use href="#i-doc"/></svg><svg><use href="#i-gear"/></svg></nav>
  </section>

  <!-- Job details -->
  <section class="screen" style="left:1130px;top:120px;height:490px">
    <div class="brand" style="top:24px"><i></i>JobRover</div>
    <div class="abs" style="left:14px;top:99px;width:230px;height:377px;background:#BDBDBD"></div>
    <div class="abs" style="left:8px;top:87px;width:230px;height:383px;background:#D0D0D0"></div>
    <article class="abs" style="left:2px;top:75px;width:230px;height:392px;background:#E6E6E6">
      <div class="abs" style="left:0;right:0;top:0;height:20px;background:var(--slate);color:var(--orange);font-size:12px;font-weight:600;text-align:center;line-height:22px">Job Details<svg class="abs" style="right:6px;top:4px;width:11px;height:11px"><use href="#i-x"/></svg></div>
      <div class="abs" style="left:0;right:0;top:20px;height:82px;background:var(--teal)">
        <div class="abs" style="left:15px;top:14px;width:54px;height:54px;border-radius:50%;background:var(--orange)"></div>
        <div class="facts" style="left:93px;width:137px;font-size:9px"><div class="lead" style="height:20px">Software Engineers</div><div class="val" style="height:23px">Singapore</div><div class="val" style="height:23px">$80 - $90 K per annum</div><div class="when">10 hrs ago</div></div>
      </div>
      <div class="abs" style="left:0;right:0;top:102px;height:80px;background:var(--orange)">
        <div class="abs" style="left:11px;top:12px;font-size:9px;font-weight:600;color:#333">Friends Working &nbsp;/ Worked Here</div>
        <div class="abs" style="left:20px;top:34px;display:flex;gap:16px;font-size:8px;color:#333;text-align:center">
          <div><span style="display:block;width:32px;height:32px;border-radius:50%;background:#eee;border:3px solid var(--teal)"></span>Mira</div>
          <div><span style="display:block;width:32px;height:32px;border-radius:50%;background:#eee;border:3px solid var(--teal)"></span>Dovan</div>
          <div><span style="display:block;width:32px;height:32px;border-radius:50%;background:#eee;border:3px solid var(--teal)"></span>Tessa</div>
        </div>
      </div>
      <div class="abs" style="left:11px;right:8px;top:188px;font-size:9px;line-height:12.9px;color:#222">
        <p>Job Desicrption</p>
        <p>Lorem ipsum dolor sit amet, consectetuer adipiscing elit, sed diam nonummy nibh euismod tincidunt ut laoreet dolore magna aliquam erat volutpat. Ut wisi enim ad minim veniam, quis nostrud exerci tation ullamcorper suscipit lobortis nisl ut aliquip ex ea commodo conse-quat. Duis autem vel eum iriure dolor in hendre-rit in vulputate velit esse molestie</p>
        <p style="margin-top:6px">Skills:</p>
        <p style="margin-top:2px">Kava, Phorge, Kava Servo, Arcline JS, Markup5</p>
      </div>
      <div class="abs" style="left:12px;top:345px;display:flex;align-items:center;gap:10px">
        <svg style="width:22px;height:22px"><use href="#i-back"/></svg>
        <svg style="width:34px;height:34px;margin-left:16px"><use href="#i-skip"/></svg>
        <svg style="width:32px;height:32px;margin-left:-2px"><use href="#i-save"/></svg>
        <svg style="width:34px;height:34px;margin-left:-4px"><use href="#i-edit"/></svg>
        <svg style="width:22px;height:22px;margin-left:14px"><use href="#i-next"/></svg>
      </div>
    </article>
  </section>

  <!-- My profile -->
  <section class="screen" style="left:36px;top:584px;height:763px">
    <div class="brand" style="top:24px"><i></i>JobRover</div>
    <div class="titlebar" style="top:85px">My Profile<svg class="back"><use href="#i-back"/></svg></div>
    <div class="abs" style="left:91px;top:129px;width:58px;height:58px;border-radius:50%;background:#eee;border:2px solid var(--orange)"></div>
    <div class="abs" style="left:0;right:0;top:189px;text-align:center;font-size:9.5px;line-height:13px;color:#444"><b style="color:#1B75BB">Jamie Tan</b><br>Singapore<br>jamie@postly.com</div>
    <div class="abs" style="left:9px;top:231px;width:173px;height:33px;background:#AAA;border:2px solid var(--mist);font-size:10px;color:#333;padding:8px 0 0 8px">Add headline to my profile</div>
    <div class="btn" style="left:190px;top:231px;width:47px;height:35px;font-size:10px">Edit</div>
    <p class="abs" style="left:7px;right:7px;top:272px;font-size:9.5px;line-height:14px;text-align:justify;color:#222">Lorem ipsum dolor sit amet, consectetuer adipiscing elit, sed diam nonummy nibh euismod tincidunt ut laoreet dolore magna aliquam erat volutpat. Ut</p>
    <div class="abs" style="left:0;right:0;top:333px;height:2px;background:#bbb"></div>
    <div class="abs" style="left:0;right:0;top:338px;height:84px;background:var(--orange);color:#fff;font-size:9.5px;line-height:13px;padding:9px 6px">
      <b style="color:#222">Work Experience</b><br>Software Engineer<br>Orbita Rocket Inc.<br>January 2015 at Present (about<br>2years)
      <div class="abs" style="left:158px;top:14px;display:flex;gap:6px"><svg style="width:24px;height:24px"><use href="#i-tplus"/></svg><svg style="width:24px;height:24px"><use href="#i-tedit"/></svg><svg style="width:24px;height:24px"><use href="#i-ttrash"/></svg></div>
    </div>
    <div class="row-list">
      <div style="top:427px">Education<svg><use href="#i-plus"/></svg></div>
      <div style="top:464px">Skills<svg><use href="#i-plus"/></svg></div>
      <div style="top:501px">Links<svg><use href="#i-plus"/></svg></div>
      <div style="top:538px">Awards<svg><use href="#i-plus"/></svg></div>
      <div style="top:575px">Certificates/Licenses<svg><use href="#i-plus"/></svg></div>
      <div style="top:612px">Patents<svg><use href="#i-plus"/></svg></div>
      <div style="top:649px">Publications<svg><use href="#i-plus"/></svg></div>
    </div>
    <nav class="nav" style="top:720px"><svg><use href="#i-home"/></svg><svg><use href="#i-search"/></svg><svg><use href="#i-target"/></svg><svg><use href="#i-doc"/></svg><svg><use href="#i-gear"/></svg></nav>
  </section>

  <!-- Modify profile -->
  <section class="screen" style="left:324px;top:584px;height:897px">
    <div class="brand" style="top:24px"><i></i>JobRover</div>
    <div class="titlebar" style="top:85px">Modify Profile<svg class="back"><use href="#i-back"/></svg></div>
    <div class="form-field" style="top:136px">First Name</div>
    <div class="form-field" style="top:198px">Last Name</div>
    <div class="form-field" style="top:260px;background:#FBDADA;border-color:#999;color:var(--alert);font-weight:400;justify-content:flex-start;gap:8px;padding-left:4px"><span style="width:26px;height:26px;border-radius:50%;background:var(--alert);color:#fff;font-weight:700;font-size:16px;text-align:center;line-height:26px">!</span>You have enterned an invalid e-mail</div>
    <div class="form-field" style="top:322px">Gender<svg style="width:22px;height:14px" viewBox="0 0 22 14"><path d="M2 2l9 9 9-9" fill="none" stroke="#F7941D" stroke-width="3"/></svg></div>
    <div class="form-field" style="top:384px">Birthday<svg style="width:24px;height:24px" viewBox="0 0 24 24"><rect x="1" y="3" width="22" height="20" fill="none" stroke="#F7941D" stroke-width="2"/><path d="M1 8h22M6 1v4M18 1v4M5 12h3M10.5 12h3M16 12h3M5 16h3M10.5 16h3M16 16h3M5 20h3M10.5 20h3" stroke="#F7941D" stroke-width="2"/></svg></div>
    <div class="form-field" style="top:446px">City</div>
    <div class="form-field" style="top:508px">State</div>
    <div class="form-field" style="top:570px">Country</div>
    <div class="abs" style="left:4px;right:4px;top:624px;height:2px;background:var(--orange)"></div>
    <div class="form-field" style="top:642px">Headline</div>
    <div class="form-field" style="top:692px;height:89px;align-items:flex-start;padding-top:2px;background:linear-gradient(90deg,#fff,#F2F4F6)">Summary</div>
    <div class="btn" style="left:81px;top:801px;width:69px;height:35px;font-size:10px">Submit</div>
    <nav class="nav" style="top:853px"><svg><use href="#i-home"/></svg><svg><use href="#i-search"/></svg><svg><use href="#i-target"/></svg><svg><use href="#i-doc"/></svg><svg><use href="#i-gear"/></svg></nav>
  </section>

  <!-- Skills -->
  <section class="screen" style="left:589px;top:584px;height:451px">
    <div class="brand" style="top:24px"><i></i>JobRover</div>
    <div class="titlebar" style="top:85px">Skills<svg class="back"><use href="#i-back"/></svg></div>
    <div class="abs" style="left:10px;top:155px;width:188px;height:36px;border:2px solid var(--teal);border-bottom-color:var(--orange);color:var(--orange);font-size:11px;font-weight:600;padding:9px 0 0 7px">*Marketing</div>
    <svg class="abs" style="left:214px;top:161px;width:24px;height:24px"><use href="#i-plus"/></svg>
    <div class="chip" style="left:12px;top:212px">Kava<svg style="width:11px;height:11px"><use href="#i-x"/></svg></div>
    <div class="chip" style="left:104px;top:212px">Markup<svg style="width:11px;height:11px"><use href="#i-x"/></svg></div>
    <div class="chip" style="left:12px;top:254px;padding-left:6px">DocuBase<svg style="width:11px;height:11px"><use href="#i-x"/></svg></div>
    <div class="chip" style="left:104px;top:254px">Pyra<svg style="width:11px;height:11px"><use href="#i-x"/></svg></div>
    <svg class="abs" style="left:96px;top:318px;width:52px;height:52px"><use href="#i-save"/></svg>
    <nav class="nav" style="top:402px"><svg><use href="#i-home"/></svg><svg><use href="#i-search"/></svg><svg><use href="#i-target"/></svg><svg><use href="#i-doc"/></svg><svg><use href="#i-gear"/></svg></nav>
  </section>

  <!-- Settings -->
  <section class="screen" style="left:858px;top:584px;height:626px">
    <div class="brand" style="top:24px"><i></i>JobRover</div>
    <div class="titlebar" style="top:85px">Settings<svg class="back"><use href="#i-back"/></svg></div>
    <div class="setting strong" style="top:140px">Notification</div>
    <div class="setting" style="top:176px">Job Message</div>
    <div class="setting" style="top:212px">Send Notification by Email too</div>
    <div class="rule" style="top:239px"></div>
    <div class="setting strong" style="top:256px">Like us on Chatterly</div>
    <div class="rule" style="top:290px"></div>
    <div class="setting strong" style="top:304px">Share on Workbrix</div>
    <div class="rule" style="top:336px"></div>
    <div class="setting strong" style="top:352px">Follow on Birdline</div>
    <div class="rule" style="top:381px"></div>
    <div class="setting strong" style="top:400px">Rate us on Appstall</div>
    <div class="rule" style="top:432px"></div>
    <div class="setting strong" style="top:448px">Help</div>
    <div class="rule" style="top:478px"></div>
    <div class="setting strong" style="top:496px">Privacy Policy</div>
    <div class="rule" style="top:520px"></div>
    <div class="setting strong" style="top:544px">Terms of use</div>
    <nav class="nav" style="top:576px"><svg><use href="#i-home"/></svg><svg><use href="#i-search"/></svg><svg><use href="#i-target"/></svg><svg><use href="#i-doc"/></svg><svg><use href="#i-gear"/></svg></nav>
  </section>

</main>
</body>
</html>
```